Rory Vandermeer | Inbound Marketing

Need a logo for a company that fills the need of creating a consistent stream of warm sales leads and revenue (via building of a sales funnel) to companies who either do not have sales teams or use outmoded outbound sales strategy to address the company bottom line. This includes Inbound marketing, SEO, content marketing strategy

Target Market(s)

Small to Medium Size Businesses, who are willing to spend thousands or tens of thousands of dollars on avertising.

Industry/Entity Type

It Company

Contact Information for Business Card

Content Strategy | PPC | SEO | Local Social & SEO
512.604.7193
roryvandermeer@quillmail.net

Logo Text

Look Inward to Gain Outward

Font styles to use
Sans Serif

Requirements
Nice to have
• I am partial to funnels in natural phenomena (tornados, whirlpools, hurricanes, black holes, spiral galaxies) but this is not a deal breaker. In fact, I don't want to intimidate anybody and seeing photos and artist representation are somewhat unsettling to me as to their vastness and darkness

```html
<!DOCTYPE html>
<html lang="en">
<head>
<meta charset="utf-8">
<title>Rory Vandermeer — Business Card</title>
<link rel="stylesheet" href="https://fonts.googleapis.com/css2?family=Roboto:wght@400;700;900&family=Roboto+Condensed:wght@400;700&display=swap">
<style>
  :root {
    --canvas-bg: #e9e6e1;
    --card-white: #ffffff;
    --card-black: #231f20;
    --ink-dark: #1c1a1b;
    --ink-light: #ffffff;
    --arc-line: #8a8687;
    --shadow: rgba(0, 0, 0, 0.18);
  }
  * { margin: 0; padding: 0; box-sizing: border-box; }
  html, body {
    width: 1200px;
    height: 1200px;
    overflow: hidden;
    background: var(--canvas-bg);
  }
  .sheet {
    width: 1200px;
    height: 1200px;
    display: flex;
    flex-direction: column;
    align-items: center;
    justify-content: center;
    gap: 80px;
  }
  .card {
    width: 660px;
    height: 377px;
    display: block;
    box-shadow: 0 12px 30px var(--shadow);
  }
  .brand-name {
    font-family: "Roboto", sans-serif;
    font-weight: 700;
    font-size: 26px;
  }
  .brand-url {
    font-family: "Roboto", sans-serif;
    font-weight: 400;
    font-size: 11px;
    letter-spacing: 2.6px;
  }
  .person-name {
    font-family: "Roboto Condensed", sans-serif;
    font-weight: 700;
    font-size: 26px;
    fill: var(--ink-dark);
  }
  .contact-line {
    font-family: "Roboto Condensed", sans-serif;
    font-weight: 400;
    font-size: 16px;
    fill: var(--ink-dark);
  }
  .service-label {
    font-family: "Roboto Condensed", sans-serif;
    font-weight: 400;
    font-size: 21px;
    fill: var(--ink-light);
  }
</style>
</head>
<body>
<main class="sheet">

  <!-- Front of card -->
  <svg class="card card-front" viewBox="0 0 660 377" xmlns="http://www.w3.org/2000/svg">
    <rect width="660" height="377" fill="var(--card-white)"/>

    <!-- curved band -->
    <path class="front-band" d="M0,272 C200,292 470,262 660,168 L660,377 L0,377 Z" fill="var(--card-black)"/>
    <path class="front-band-stripe" d="M0,318 C220,334 500,304 660,214" fill="none" stroke="var(--card-white)" stroke-width="6"/>

    <!-- brand -->
    <g class="brand">
      <circle cx="68" cy="172" r="22" fill="var(--ink-dark)"/>
      <text class="brand-name" x="98" y="182" fill="var(--ink-dark)">Rory Vandermeer</text>
      <text class="brand-url" x="100" y="201" fill="var(--ink-dark)">www.roryvandermeer.com</text>
    </g>

    <!-- contact -->
    <g class="contact">
      <text class="person-name" x="372" y="88">RORY VANDERMEER</text>

      <g class="icon-phone" transform="translate(374,110)" fill="var(--ink-dark)">
        <path d="M2,5 C2,2 5,0 8,0 L12,0 C15,0 18,2 18,5 L14,6 L13,3 L7,3 L6,6 Z"/>
        <path d="M4,8 L16,8 L18,16 L2,16 Z"/>
      </g>
      <text class="contact-line" x="400" y="124">512.604.7193</text>

      <g class="icon-mail" transform="translate(374,138)">
        <rect x="0" y="0" width="18" height="13" fill="var(--ink-dark)"/>
        <path d="M0,0 L9,7 L18,0" fill="none" stroke="var(--card-white)" stroke-width="1.5"/>
      </g>
      <text class="contact-line" x="400" y="151">roryvandermeer@quillmail.net</text>
    </g>
  </svg>

  <!-- Back of card -->
  <svg class="card card-back" viewBox="0 0 660 377" xmlns="http://www.w3.org/2000/svg">
    <rect width="660" height="377" fill="var(--card-black)"/>

    <!-- service arc -->
    <path class="service-arc" d="M102.8,215 A170,170 0 0 1 409.7,241.9" fill="none" stroke="var(--arc-line)" stroke-width="1.2"/>
    <g class="service-points" fill="var(--ink-light)">
      <circle cx="152.5" cy="160.7" r="7"/>
      <circle cx="235.2" cy="130.6" r="7"/>
      <circle cx="321.8" cy="145.9" r="7"/>
      <circle cx="389.3" cy="202.5" r="7"/>
    </g>
    <g class="service-labels">
      <text class="service-label" transform="translate(166,152) rotate(-45)">Content Strategy</text>
      <text class="service-label" transform="translate(249,122) rotate(-45)">PPC</text>
      <text class="service-label" transform="translate(336,137) rotate(-45)">SEO</text>
      <text class="service-label" transform="translate(403,194) rotate(-45)">Local Social &amp; SEO</text>
    </g>

    <!-- brand -->
    <g class="brand">
      <circle cx="140" cy="292" r="22" fill="var(--ink-light)"/>
      <text class="brand-name" x="170" y="302" fill="var(--ink-light)">Rory Vandermeer</text>
      <text class="brand-url" x="172" y="321" fill="var(--ink-light)">www.roryvandermeer.com</text>
    </g>
  </svg>

</main>
</body>
</html>
```